Etiketten für Rotwein
Zielgruppe
Wir starten dieses Jahr mit unserem ersten Rotwein unserer neuen Marke CAL VERDUNES aus unserem neuen Weingut auf Mallorca.
Es folgen in den kommenden Jahren ein Rosé und weitere Weißweine.
Aufgabenstellung
Wir suchen ein Design für unser erstes Flaschenetikett der Rotweinflaschen.
Die Höhe soll maximal 130 mm sein.
Der Name soll 'Bertoldo' sein.
Die Rebsorte 'Cabernet Sauvignon' und der Jahrgang '2025' sollen mit erscheinen.
Unser Logo sollte mit integriert werden.
Das Erscheinungsbild soll edel, elegant, markant, präsent, wieder erkennbar und einzigartig sein.
Es gibt ein paar Ideen, diese sind aber nur als Hinweise zu verstehen, die verwendet werden könnten.
Dies sind 2 Teddybären im Weinfeld, Teddybären auf einem Traktor im Weinfeld/ Weinberg, Landschaft oder eben komplett etwas anderes Kreatives.
Die Anlagen sind unser Logo in 3 Varianten und einige Beispiele von eigenen unprofessionellen Versuchen, sowie tolle Etikettendesigns die uns gefallen.
We are looking for a design for our first red wine bottle label.
The maximum height should be 130mm.
The name should be 'Bertoldo'.
The grape variety 'Cabernet Sauvignon' and the vintage 2025 should also be included.
Our logo should be integrated.
The overall look should be sophisticated, elegant, striking, memorable, recognizable, and unique.
We have a few ideas, but these are just suggestions that could be used.
These include two teddy bears in a vineyard, teddy bears on a tractor in a vineyard, a landscape, or something completely different and creative.
Attached are our logo in three variations, some examples of our own unprofessional attempts, and some great label designs that we like.
Jens & Uwe
Cal Verdunes

```html
<!DOCTYPE html>
<html lang="de">
<head>
<meta charset="utf-8">
<title>Bertoldo – Cabernet Sauvignon 2025</title>
<link rel="stylesheet" href="https://fonts.googleapis.com/css2?family=Libre+Caslon+Display&family=Montserrat:wght@500;600&display=swap">
<style>
  :root {
    --wine-deep: #3a0f0c;
    --wine-mid: #5a1c15;
    --wine-warm: #6e2a1c;
    --leaf-rust: #8a3a22;
    --gold-light: #f3d67a;
    --gold: #d9a93d;
    --gold-dark: #a8761f;
    --cream-gold: #f0dfae;
  }
  * { margin: 0; padding: 0; box-sizing: border-box; }
  html, body {
    width: 800px;
    height: 1200px;
    overflow: hidden;
    background: var(--wine-deep);
  }
  .label {
    position: relative;
    width: 800px;
    height: 1200px;
    overflow: hidden;
    background:
      radial-gradient(ellipse at 50% 35%, var(--wine-mid) 0%, var(--wine-deep) 75%);
  }
  .vine-pattern {
    position: absolute;
    left: 0;
    top: 360px;
    width: 800px;
    height: 840px;
    background:
      radial-gradient(ellipse 70% 22% at 50% 18%, rgba(138,58,34,0.55) 0%, rgba(138,58,34,0) 100%),
      radial-gradient(ellipse 60% 30% at 50% 80%, rgba(110,42,28,0.35) 0%, rgba(110,42,28,0) 100%);
  }
  .brand-seal {
    position: absolute;
    left: 244px;
    top: 148px;
    width: 336px;
    height: 336px;
  }
  .brand-seal svg { position: absolute; inset: 0; }
  .brand-name {
    position: absolute;
    left: 0;
    right: 0;
    top: 154px;
    text-align: center;
    font-family: "Montserrat", sans-serif;
    font-weight: 600;
    font-size: 26px;
    letter-spacing: 0.5px;
    color: var(--gold);
  }
  .wine-name {
    position: absolute;
    left: 0;
    right: 0;
    top: 672px;
    text-align: center;
    font-family: "Libre Caslon Display", serif;
    font-size: 150px;
    line-height: 1;
    background: linear-gradient(180deg, var(--gold-light) 0%, var(--gold) 55%, var(--gold-dark) 100%);
    -webkit-background-clip: text;
    background-clip: text;
    color: transparent;
    filter: drop-shadow(0 3px 3px rgba(0,0,0,0.45));
  }
  .divider {
    position: absolute;
    left: 160px;
    top: 876px;
    width: 480px;
    height: 2px;
    background: linear-gradient(90deg, rgba(217,169,61,0) 0%, var(--gold) 12%, var(--gold) 88%, rgba(217,169,61,0) 100%);
  }
  .varietal-vintage {
    position: absolute;
    left: 0;
    right: 0;
    top: 908px;
    text-align: center;
    font-family: "Montserrat", sans-serif;
    font-weight: 500;
    font-size: 23px;
    letter-spacing: 1.5px;
    color: var(--cream-gold);
  }
</style>
</head>
<body>
  <main class="label">
    <div class="vine-pattern" role="img" aria-label="Embossed pattern of sweeping vine leaves and vineyard rows in rust tones"></div>

    <div class="brand-seal">
      <svg width="336" height="336" viewBox="0 0 336 336" aria-hidden="true">
        <defs>
          <linearGradient id="ringGold" x1="0" y1="0" x2="1" y2="1">
            <stop offset="0" stop-color="#f3d67a"/>
            <stop offset="0.5" stop-color="#d9a93d"/>
            <stop offset="1" stop-color="#a8761f"/>
          </linearGradient>
        </defs>
        <circle cx="168" cy="168" r="164" fill="#4a1410" fill-opacity="0.55" stroke="url(#ringGold)" stroke-width="3"/>
      </svg>
      <p class="brand-name">CAL VERDUNES</p>
    </div>

    <h1 class="wine-name">Bertoldo</h1>
    <div class="divider"></div>
    <p class="varietal-vintage">CABERNET SAUVIGNON • 2025</p>
  </main>
</body>
</html>
```